Veltorix needs web site design

We need a web site design for our product called 'Veltorix'. We develop an asset management system that can manage all kind of assets. Currently we have a logo theme and would like to use similar color scheme; the content concept is pretty much in http://tbaldwyn.example but the product was called "Keystone Lab" at the time and is now called "Veltorix". Velto means Unified Ledger Tracking Operations Network Agency.
Please use generic image for asset (not just bridges) e.g buildings, trucks, powerlines. train, bus, lightrail etc..
Please emphazise on the data management and security, and distributed networking.

the new website address is https://www.veltorix.example/

name on business card

Thomas Baldwyn 555-014-7723
Principal Architect / Software Engineer

Dana Baldwyn 555-018-2946
Software Engineer

Coding

Coded - Design and coding required

Number of Pages Required

1 page

```html
<!DOCTYPE html>
<html lang="en">
<head>
<meta charset="utf-8">
<title>Veltorix Asset Management</title>
<link href="https://fonts.googleapis.com/css2?family=Montserrat:wght@400;500;600;700&family=Arimo:wght@400;700&display=swap" rel="stylesheet">
<style>
:root{
  --navy:#1b1c7d;
  --navy-deep:#0a0c6e;
  --gold:#c4952e;
  --ink:#333;
  --muted:#555;
  --soft:#f3f3f3;
  --white:#fff;
}
*{margin:0;padding:0;box-sizing:border-box}
html,body{width:1200px;height:2946px;overflow:hidden;background:var(--white)}
body{position:relative;font-family:Arimo,Arial,sans-serif;color:var(--ink)}
.abs{position:absolute}

/* header */
.site-header{left:0;top:0;width:1200px;height:114px;background:var(--white)}
.quick-contact{left:720px;top:0;width:480px;height:44px;background:var(--gold);clip-path:polygon(28px 0,100% 0,100% 100%,0 100%);color:var(--white);font:500 14.5px Montserrat,sans-serif;display:flex;align-items:center;padding-left:56px;gap:10px}
.brand-mark{left:86px;top:32px;width:54px;height:52px;border:4px solid var(--navy);background:var(--white)}
.brand-name{left:150px;top:28px;font:700 38px/1 Montserrat,sans-serif;color:var(--navy)}
.brand-tag{left:150px;top:66px;font:500 15.5px/1 Montserrat,sans-serif;color:var(--navy);letter-spacing:.4px;white-space:nowrap}
.main-nav{top:76px;left:540px;font:500 12.5px Montserrat,sans-serif;color:#222}
.main-nav span{position:absolute;white-space:nowrap}
.main-nav .active{color:var(--gold)}

/* hero */
.hero{left:0;top:114px;width:1200px;height:544px;background:linear-gradient(135deg,#a9b3bd 0%,#6f7884 35%,#3c434c 65%,#1f252d 100%)}
.hero-arrow{width:36px;height:36px;border:2px solid var(--white);border-radius:50%;top:367px}
.hero-label{left:400px;top:420px;width:400px;height:50px;background:var(--gold);color:var(--white);font:600 20px/50px Montserrat,sans-serif;text-align:center;letter-spacing:.5px;white-space:nowrap}
.hero-sub{left:262px;top:480px;width:676px;height:50px;background:var(--navy);color:var(--white);font:600 16.5px/50px Montserrat,sans-serif;text-align:center;white-space:nowrap;overflow:hidden}

/* section titles */
.section-title{width:1200px;left:0;text-align:center;font:400 29px Montserrat,sans-serif;color:var(--navy)}
.title-rule{width:70px;height:2px;background:var(--gold)}
.section-lead{width:1200px;left:0;text-align:center;font:400 12.5px Arimo,sans-serif;color:var(--ink)}

/* services */
.service-card{top:890px;width:234px;height:245px;color:var(--white);text-align:center;box-shadow:0 14px 14px -8px rgba(0,0,0,.25)}
.service-card.navy{background:var(--navy)}
.service-card.gold{background:var(--gold)}
.service-icon{position:absolute;left:50%;top:-58px;width:134px;height:134px;margin-left:-67px;border-radius:50%;background:var(--white);border:4px solid currentColor;display:flex;align-items:center;justify-content:center}
.service-card.navy .service-icon{color:var(--navy)}
.service-card.gold .service-icon{color:var(--gold)}
.service-title{position:absolute;left:10px;right:10px;font:600 13.5px/20px Montserrat,sans-serif}
.service-rule{position:absolute;left:89px;width:56px;height:2px;background:var(--white)}
.service-text{position:absolute;left:6px;right:6px;top:152px;font:400 12px/22px Arimo,sans-serif}

/* welcome */
.welcome{left:0;top:1200px;width:1200px;height:417px;background:var(--soft)}
.welcome-photo{left:86px;top:1242px;width:482px;height:332px;background:linear-gradient(120deg,#0b1c4a 0%,#1f4f9e 45%,#5aa0e0 60%,#1a2c5c 100%)}
.welcome-title{left:625px;top:1252px;font:400 29px Montserrat,sans-serif;color:var(--navy)}
.welcome-text{left:630px;top:1333px;width:435px;font:400 12px/25.6px Arimo,sans-serif;color:var(--muted)}
.btn-navy{left:630px;top:1520px;width:122px;height:43px;background:var(--navy);color:var(--white);font:600 12px/43px Montserrat,sans-serif;text-align:center}

/* call to action */
.cta{left:0;top:1617px;width:1200px;height:358px;background:linear-gradient(90deg,#5a4c40 0%,#8a7a6a 35%,#76695c 60%,#3f4548 100%)}
.cta-title{width:1200px;left:0;top:1733px;text-align:center;color:var(--white);font:600 25px Montserrat,sans-serif}
.cta-sub{width:1200px;left:0;top:1772px;text-align:center;color:var(--white);font:400 24px Montserrat,sans-serif}
.btn-gold{left:515px;top:1824px;width:171px;height:48px;background:var(--gold);color:var(--white);font:500 19px/48px Montserrat,sans-serif;text-align:center}

/* blog */
.blog-card{top:2140px;width:332px;height:428px;background:var(--white);border:1px solid #e2e2e2;box-shadow:0 0 6px rgba(0,0,0,.08);text-align:center}
.blog-photo{height:225px;width:100%}
.blog-title{margin-top:30px;font:500 15px Montserrat,sans-serif;color:#333}
.blog-date{margin-top:17px;font:500 14.5px Montserrat,sans-serif;color:var(--gold);display:flex;justify-content:center;align-items:center;gap:8px}
.blog-text{margin:14px 22px 0;font:400 12px/25.5px Arimo,sans-serif;color:var(--muted)}

/* footer */
.site-footer{left:0;top:2628px;width:1200px;height:318px;background:var(--navy-deep)}
.social{top:2657px;width:59px;height:59px;border:1.5px solid rgba(255,255,255,.8);border-radius:50%}
.contact-icon{top:2770px;width:54px;height:54px;border:1.5px solid var(--white);border-radius:50%;display:flex;align-items:center;justify-content:center}
.contact-block{top:2774px;color:var(--white)}
.contact-label{font:500 18px/24px Montserrat,sans-serif;color:var(--white)}
.contact-value{font:600 12.5px/22px Montserrat,sans-serif;color:var(--white)}
.footer-rule{left:86px;top:2870px;width:1028px;height:1px;background:rgba(255,255,255,.15)}
.copyright{width:1200px;left:0;top:2900px;text-align:center;font:400 12.5px Arimo,sans-serif;color:var(--white)}
</style>
</head>
<body>

<header class="abs site-header">
  <div class="abs quick-contact">
    <svg width="14" height="14" viewBox="0 0 24 24" fill="#fff"><path d="M6.6 10.8a15 15 0 0 0 6.6 6.6l2.2-2.2a1 1 0 0 1 1-.25 11.4 11.4 0 0 0 3.6.57 1 1 0 0 1 1 1V20a1 1 0 0 1-1 1A17 17 0 0 1 3 4a1 1 0 0 1 1-1h3.5a1 1 0 0 1 1 1c0 1.25.2 2.45.57 3.57a1 1 0 0 1-.25 1z"/></svg>
    QUICK CONTACT : 555-014-7723 / 555-018-2946
  </div>
  <div class="abs brand-mark"></div>
  <div class="abs brand-name">Veltorix</div>
  <div class="abs brand-tag">ASSET MANAGEMENT</div>
  <nav class="abs main-nav">
    <span class="active" style="left:0">HOME</span>
    <span style="left:84px">SERVICES</span>
    <span style="left:189px">PORTFOLIO</span>
    <span style="left:306px">DOWNLOAD</span>
    <span style="left:426px">ABOUT</span>
    <span style="left:516px">CONTACT</span>
  </nav>
</header>

<section class="abs hero" role="img" aria-label="Business team in suits shaking hands and applauding in a bright office"></section>
<div class="abs hero-arrow" style="left:42px"><svg width="32" height="32" viewBox="0 0 32 32"><path d="M18 10l-6 6 6 6" stroke="#fff" stroke-width="2.5" fill="none"/></svg></div>
<div class="abs hero-arrow" style="left:1121px"><svg width="32" height="32" viewBox="0 0 32 32"><path d="M14 10l6 6-6 6" stroke="#fff" stroke-width="2.5" fill="none"/></svg></div>
<div class="abs hero-label">VELTORIX ASSET MANAGEMENT</div>
<div class="abs hero-sub">SED UT PERSPICIATIS UNDE OMNIS ISTE NATUS ERROR SIT VOLUPTATEM</div>

<h2 class="abs section-title" style="top:693px">OUR SERVICES</h2>
<div class="abs title-rule" style="left:565px;top:741px"></div>
<p class="abs section-lead" style="top:770px">Baldwyn and Partners is a software development firm since 1989, specializing in structural engineering</p>

<div class="abs service-card navy" style="left:86px">
  <div class="service-icon"><svg width="70" height="70" viewBox="0 0 70 70" fill="none" stroke="currentColor" stroke-width="2.5"><rect x="14" y="14" width="42" height="30" rx="2"/><path d="M8 52h54l-4-8H12z"/><path d="M31 22l-4 7 4 7M39 22l4 7-4 7"/></svg></div>
  <div class="service-title" style="top:102px">SOFTWARE DEVELOPMENT</div>
  <div class="service-rule" style="top:136px"></div>
  <p class="service-text">Sed ut perspiciatis unde omnis iste natus error sit voluptatem accusantium beatae vitae dicta sunt explicabo.</p>
</div>
<div class="abs service-card gold" style="left:350px">
  <div class="service-icon"><svg width="74" height="74" viewBox="0 0 74 74" fill="none" stroke="currentColor" stroke-width="2.5"><rect x="6" y="30" width="14" height="12"/><rect x="48" y="10" width="18" height="12"/><rect x="48" y="31" width="18" height="12"/><rect x="48" y="52" width="18" height="12"/><rect x="28" y="30" width="10" height="12"/><path d="M20 36h8M38 36h10M43 16v42M43 16h5M43 58h5"/></svg></div>
  <div class="service-title" style="top:102px">WEB AND NETWORK</div>
  <div class="service-rule" style="top:136px"></div>
  <p class="service-text">Sed ut perspiciatis unde omnis iste natus error sit voluptatem accusantium beatae vitae dicta sunt explicabo.</p>
</div>
<div class="abs service-card navy" style="left:614px">
  <div class="service-icon"><svg width="70" height="70" viewBox="0 0 70 70" fill="none" stroke="currentColor" stroke-width="2.5"><rect x="10" y="12" width="50" height="34" rx="2"/><path d="M28 46v8M42 46v8M20 56h30"/><rect x="18" y="20" width="20" height="14"/><path d="M44 22h10M44 28h10M44 34h6"/></svg></div>
  <div class="service-title" style="top:88px">SOFTWARE PROJECT<br>MANAGEMENT</div>
  <div class="service-rule" style="top:136px"></div>
  <p class="service-text">Sed ut perspiciatis unde omnis iste natus error sit voluptatem accusantium beatae vitae dicta sunt explicabo.</p>
</div>
<div class="abs service-card gold" style="left:878px">
  <div class="service-icon"><svg width="70" height="70" viewBox="0 0 70 70" fill="none" stroke="currentColor" stroke-width="2.5"><rect x="10" y="10" width="50" height="46"/><path d="M10 18h50"/><circle cx="24" cy="30" r="4"/><circle cx="35" cy="30" r="4"/><circle cx="46" cy="30" r="4"/><path d="M18 50v-8a6 6 0 0 1 12 0v8M29 50v-8a6 6 0 0 1 12 0v8M40 50v-8a6 6 0 0 1 12 0v8"/></svg></div>
  <div class="service-title" style="top:102px">COMPUTING CONSULTANT</div>
  <div class="service-rule" style="top:136px"></div>
  <p class="service-text">Sed ut perspiciatis unde omnis iste natus error sit voluptatem accusantium beatae vitae dicta sunt explicabo.</p>
</div>

<section class="abs welcome"></section>
<div class="abs welcome-photo" role="img" aria-label="Businessman touching a glowing gear interface labelled asset management"></div>
<h2 class="abs welcome-title">WELCOME TO VELTORIX</h2>
<div class="abs title-rule" style="left:628px;top:1305px"></div>
<p class="abs welcome-text">Sed ut perspiciatis unde omnis iste natus error sit voluptatem accusantium dol oremque laudantium, totam rem aperiam, eaque ipsa quae ab illo inventore veri tatis et quasi architecto beatae vitae dicta sunt explicabo. Nemo enim ipsam voluptatem quia voluptas sit aspernatur aut odit aut fugit, sed quia consequuntur magni dolores eos qui ratione voluptatem sequi nesciunt.Neque porro quisquam est, qui dolorem ipsum quia dolor sit amet, consectetur, adipisci</p>
<div class="abs btn-navy">READ MORE</div>

<section class="abs cta" role="img" aria-label="Smiling business partners shaking hands across a table"></section>
<h2 class="abs cta-title">SED UT PERSPICIATIS UNDE OMNIS ISTE</h2>
<p class="abs cta-sub">error sit voluptatem accusantium doloremque laudantium</p>
<div class="abs btn-gold">Read More</div>

<h2 class="abs section-title" style="top:2013px">LATEST BLOG</h2>
<div class="abs title-rule" style="left:560px;top:2067px"></div>
<p class="abs section-lead" style="top:2088px">Sed ut perspiciatis unde omnis iste natus error sit voluptatem accusantium doloremque laudantium</p>

<article class="abs blog-card" style="left:86px">
  <div class="blog-photo" role="img" aria-label="Hands working on a laptop at a wooden desk" style="background:linear-gradient(135deg,#4a3a2c,#a07a55 55%,#d9c4a5)"></div>
  <h3 class="blog-title">SED UT PERSPICIATIS UNDE</h3>
  <div class="blog-date"><svg width="13" height="13" viewBox="0 0 14 14" fill="none" stroke="#c4952e" stroke-width="1.5"><rect x="1" y="2.5" width="12" height="10.5"/><path d="M1 6h12M4 1v3M10 1v3"/></svg>JUNE 20, 2018</div>
  <p class="blog-text">Sed ut perspiciatis unde omnis iste natus error sit voluptatem accusantium doloremque laudantium,rem aperiam, eaque ipsa quae ab</p>
</article>
<article class="abs blog-card" style="left:434px">
  <div class="blog-photo" role="img" aria-label="Close-up of metal gears" style="background:linear-gradient(135deg,#2b2b2b,#8a8a8a 50%,#3a3a3a)"></div>
  <h3 class="blog-title">SED UT PERSPICIATIS UNDE</h3>
  <div class="blog-date"><svg width="13" height="13" viewBox="0 0 14 14" fill="none" stroke="#c4952e" stroke-width="1.5"><rect x="1" y="2.5" width="12" height="10.5"/><path d="M1 6h12M4 1v3M10 1v3"/></svg>JUNE 20, 2018</div>
  <p class="blog-text">Sed ut perspiciatis unde omnis iste natus error sit voluptatem accusantium doloremque laudantium,rem aperiam, eaque ipsa quae ab</p>
</article>
<article class="abs blog-card" style="left:782px">
  <div class="blog-photo" role="img" aria-label="Person facing a glowing digital network over a city at night" style="background:linear-gradient(180deg,#1b2350,#3c4f8a 50%,#141a30)"></div>
  <h3 class="blog-title">SED UT PERSPICIATIS UNDE</h3>
  <div class="blog-date"><svg width="13" height="13" viewBox="0 0 14 14" fill="none" stroke="#c4952e" stroke-width="1.5"><rect x="1" y="2.5" width="12" height="10.5"/><path d="M1 6h12M4 1v3M10 1v3"/></svg>JUNE 20, 2018</div>
  <p class="blog-text">Sed ut perspiciatis unde omnis iste natus error sit voluptatem accusantium doloremque laudantium,rem aperiam, eaque ipsa quae ab</p>
</article>

<footer class="abs site-footer"></footer>
<div class="abs social" style="left:391px" aria-label="Social link"></div>
<div class="abs social" style="left:463px" aria-label="Social link"></div>
<div class="abs social" style="left:534px" aria-label="Social link"></div>
<div class="abs social" style="left:606px" aria-label="Social link"></div>
<div class="abs social" style="left:676px" aria-label="Social link"></div>
<div class="abs social" style="left:748px;display:flex;align-items:center;justify-content:center" aria-label="Email"><svg width="18" height="14" viewBox="0 0 18 14" fill="none" stroke="#fff" stroke-width="1.5"><rect x="1" y="1" width="16" height="12" rx="1"/><path d="M1 2l8 6 8-6"/></svg></div>

<div class="abs contact-icon" style="left:119px"><svg width="16" height="20" viewBox="0 0 16 20" fill="#fff"><path d="M8 0a7 7 0 0 0-7 7c0 5 7 13 7 13s7-8 7-13a7 7 0 0 0-7-7zm0 10a3 3 0 1 1 0-6 3 3 0 0 1 0 6z"/></svg></div>
<div class="abs contact-block" style="left:188px"><div class="contact-label">Address :</div><div class="contact-value">P. O. Box 40417<br>Lakeview, WA 98000-1200</div></div>
<div class="abs contact-icon" style="left:513px"><svg width="18" height="14" viewBox="0 0 18 14" fill="none" stroke="#fff" stroke-width="1.5"><rect x="1" y="1" width="16" height="12" rx="1"/><path d="M1 2l8 6 8-6"/></svg></div>
<div class="abs contact-block" style="left:582px"><div class="contact-label">Email</div><div class="contact-value">support@Veltorix.com</div></div>
<div class="abs contact-icon" style="left:865px"><svg width="18" height="18" viewBox="0 0 24 24" fill="#fff"><path d="M6.6 10.8a15 15 0 0 0 6.6 6.6l2.2-2.2a1 1 0 0 1 1-.25 11.4 11.4 0 0 0 3.6.57 1 1 0 0 1 1 1V20a1 1 0 0 1-1 1A17 17 0 0 1 3 4a1 1 0 0 1 1-1h3.5a1 1 0 0 1 1 1c0 1.25.2 2.45.57 3.57a1 1 0 0 1-.25 1z"/></svg></div>
<div class="abs contact-block" style="left:934px"><div class="contact-label">Phone</div><div class="contact-value">Mobile :&nbsp; 555-014-7723</div></div>
<div class="abs footer-rule"></div>
<p class="abs copyright">© Copyright-2018 Veltorix All rights reserved</p>

</body>
</html>
```